Business card design needed

We do excavation, cartage and contracting
I would quote like to have a picture of my digger as the whole back ground and the words on top. If that looks any good
Otherwise please feel free to come up with any other cool options

Cheers Marc

KLR Contracting
Excavation, Cartage, Contracting
Marcus Prewitt
www.klr-example.co.nz
021 584 067
marc@klr-example.co.nz

```html
<!DOCTYPE html>
<html lang="en">
<head>
<meta charset="utf-8">
<title>KLR Contracting — Business Card</title>
<link rel="stylesheet" href="https://fonts.googleapis.com/css2?family=Open+Sans:wght@300;400;700&display=swap">
<style>
  :root {
    --brand-green: #17552f;
    --paper: #ffffff;
    --backdrop-tone: #f4f5f3;
  }
  html, body {
    margin: 0;
    padding: 0;
    width: 1200px;
    height: 752px;
    overflow: hidden;
    background: var(--paper);
  }
  .card {
    position: relative;
    width: 1200px;
    height: 752px;
    background: var(--paper);
    font-family: "Open Sans", Arial, sans-serif;
    color: var(--brand-green);
    overflow: hidden;
  }
  .digger-backdrop {
    position: absolute;
    left: 0;
    top: 0;
    width: 880px;
    height: 752px;
    background: radial-gradient(ellipse at 45% 45%, var(--backdrop-tone) 0%, var(--paper) 72%);
  }
  .contact {
    position: absolute;
    right: 73px;
    top: 44px;
    text-align: right;
  }
  .contact__name {
    margin: 0;
    font-weight: 700;
    font-size: 40px;
    letter-spacing: 0.17em;
    line-height: 1;
    margin-right: -0.17em;
  }
  .contact__line {
    display: flex;
    justify-content: flex-end;
    align-items: center;
    gap: 10px;
    font-weight: 300;
    font-size: 20px;
    letter-spacing: 0.22em;
    margin-right: -0.22em;
  }
  .contact__line--email { margin-top: 18px; }
  .contact__line--phone { margin-top: 8px; letter-spacing: 0.08em; margin-right: -0.08em; }
  .brand {
    position: absolute;
    left: 40px;
    top: 232px;
    width: 660px;
    text-align: center;
  }
  .brand__name {
    margin: 0;
    font-weight: 700;
    font-size: 120px;
    line-height: 150px;
    letter-spacing: 0.02em;
  }
  .brand__tagline {
    margin: 20px 0 0;
    font-weight: 400;
    font-size: 28px;
    line-height: 1.1;
  }
  .brand__web {
    margin: 8px 0 0;
    font-weight: 300;
    font-size: 22px;
    letter-spacing: 0.2em;
  }
</style>
</head>
<body>
  <main class="card">
    <div class="digger-backdrop" role="img" aria-label="Faint dotted outline of an excavator digger filling the background"></div>

    <section class="contact">
      <h1 class="contact__name">Marcus Prewitt</h1>
      <div class="contact__line contact__line--email">
        <svg width="33" height="20" viewBox="0 0 33 20" aria-hidden="true">
          <rect x="1" y="1" width="31" height="18" fill="none" stroke="var(--brand-green)" stroke-width="2"/>
          <path d="M1 1 L16.5 12 L32 1 M1 19 L12 9 M32 19 L21 9" fill="none" stroke="var(--brand-green)" stroke-width="2"/>
        </svg>
        <span>marc@klr-example.co.nz</span>
      </div>
      <div class="contact__line contact__line--phone">
        <svg width="46" height="46" viewBox="0 0 46 46" aria-hidden="true">
          <circle cx="23" cy="23" r="23" fill="var(--brand-green)"/>
          <rect x="12" y="11" width="8" height="24" rx="2" fill="none" stroke="#fff" stroke-width="2"/>
          <rect x="21" y="14" width="13" height="21" rx="1" fill="none" stroke="#fff" stroke-width="2"/>
          <rect x="24" y="17" width="7" height="4" fill="#fff"/>
          <g fill="#fff">
            <rect x="24" y="24" width="2" height="2"/><rect x="28" y="24" width="2" height="2"/>
            <rect x="24" y="28" width="2" height="2"/><rect x="28" y="28" width="2" height="2"/>
          </g>
        </svg>
        <span>021 584 067</span>
      </div>
    </section>

    <section class="brand">
      <p class="brand__name">KLR</p>
      <p class="brand__tagline">Contracting Excavation . Cartage .&nbsp; Contracting</p>
      <p class="brand__web">www.klr-example.co.nz</p>
    </section>
  </main>
</body>
</html>
```